Jewelry Wholesale Business Card Design

Company name: VELORA
Business Background: Wholesale jewelry store located in downtown Los Angeles. We specialize in 18k gold-filled, stainless steel, 14kt gold, and natural stone jewelry.
website: www.velorashop.example
Instagram: velora_
Email: sales@velorashop.example
Address: 318 W. PRIOR ST #27, #109
LOS ANGELES, CA 90099
(213)555-0147

We would like to create a simple, yet elegant business card for my store
-Includes company logo
-Black background preferred
-Gold metallic color letters
- Lists the type of products we sell
-Small icons for instagram handle, phone, email, and website

Target Market(s)

Hispanic community, age 12-40

Industry/Entity Type

Jewelry Wholesale

Contact Information for Business Card

logo, business location, website, phone number, email, instagram, lists type of products, Dylan Morvet(my name)

Font styles to use
Serif
Sans Serif

Colors
FFF300
FFF600
FEFA6F
FFFEC7
FFFEE8

Requirements
Must have
• logo, business location, website, phone number, email, instagram, lists type of products, Dylan Morvet(my name)

```html
<!DOCTYPE html>
<html lang="en">
<head>
<meta charset="utf-8">
<title>VELORA Business Card</title>
<link rel="stylesheet" href="https://fonts.googleapis.com/css2?family=Cinzel:wght@500&family=Arimo:wght@400&display=swap">
<style>
  :root {
    --stage: #e4e4e4;
    --card-black: #050505;
    --card-white: #f7f7f7;
    --gold: #ffe000;
    --gold-soft: #fef36f;
    --ink: #111111;
    --tagline: #f2f2f2;
  }
  * { box-sizing: border-box; margin: 0; padding: 0; }
  html, body {
    width: 1200px; height: 930px; overflow: hidden;
    background: var(--stage);
  }
  .sheet {
    width: 1200px; height: 930px;
    display: flex; flex-direction: column;
    align-items: center; justify-content: center; gap: 44px;
  }
  .card {
    width: 640px; height: 366px;
    position: relative; overflow: hidden;
    box-shadow: 0 6px 18px rgba(0,0,0,0.12);
  }

  /* Front */
  .card-front { background: var(--card-black); }
  .wordmark {
    position: absolute; top: 118px; left: 0; right: 0;
    text-align: center;
    font-family: "Cinzel", serif; font-weight: 500;
    font-size: 84px; letter-spacing: 2px; line-height: 1;
    color: var(--gold);
  }
  .product-line {
    position: absolute; left: 34px; right: 34px; bottom: 34px;
    font-family: "Arimo", sans-serif; font-size: 15.5px;
    color: var(--tagline); letter-spacing: 0.3px;
    display: flex; align-items: center; gap: 8px; white-space: nowrap;
  }
  .product-line .sep {
    width: 6px; height: 6px; background: var(--gold);
    transform: rotate(45deg); flex: none;
  }

  /* Back */
  .card-back { background: var(--card-white); display: flex; }
  .brand-panel {
    width: 228px; height: 100%;
    background: var(--card-black);
    display: flex; align-items: center; justify-content: center;
  }
  .brand-panel .panel-name {
    font-family: "Cinzel", serif; font-weight: 500;
    font-size: 34px; letter-spacing: 1px; color: var(--gold);
  }
  .contact {
    flex: 1; padding: 62px 0 0 48px;
    font-family: "Arimo", sans-serif; color: var(--ink);
  }
  .contact-name {
    font-family: "Cinzel", serif; font-weight: 500;
    font-size: 27px; letter-spacing: 1.5px; margin-bottom: 14px;
  }
  .contact-list { list-style: none; }
  .contact-list li {
    display: flex; align-items: center; gap: 10px;
    font-size: 17px; line-height: 25px;
  }
  .contact-list svg { width: 16px; height: 16px; flex: none; }
  .address {
    margin-top: 14px; font-size: 17px; line-height: 23px;
    text-transform: uppercase; letter-spacing: 0.3px;
  }
</style>
</head>
<body>
<main class="sheet">

  <section class="card card-front" aria-label="Card front">
    <h1 class="wordmark">VELORA</h1>
    <p class="product-line">
      <span>18k gold-filled</span><span class="sep"></span>
      <span>Stainless steel</span><span class="sep"></span>
      <span>14kt gold</span><span class="sep"></span>
      <span>Natural stone jewelry.</span>
    </p>
  </section>

  <section class="card card-back" aria-label="Card back">
    <div class="brand-panel">
      <span class="panel-name">VELORA</span>
    </div>
    <div class="contact">
      <h2 class="contact-name">DYLAN MORVET</h2>
      <ul class="contact-list">
        <li>
          <svg viewBox="0 0 16 16" aria-hidden="true"><path d="M4 1.5 L6.5 4.5 L5 6.3 Q6.5 9.5 9.7 11 L11.5 9.5 L14.5 12 L13 14.3 Q7.5 14.5 4 11 Q0.8 7.5 1.7 3 Z" fill="none" stroke="#111" stroke-width="1.4" stroke-linejoin="round"/></svg>
          <span>(213)555-0147</span>
        </li>
        <li>
          <svg viewBox="0 0 16 16" aria-hidden="true"><rect x="1" y="3.5" width="14" height="9.5" fill="#111"/><path d="M1.5 4 L8 9 L14.5 4" fill="none" stroke="#f7f7f7" stroke-width="1.2"/></svg>
          <span>sales@velorashop.example</span>
        </li>
        <li>
          <svg viewBox="0 0 16 16" aria-hidden="true"><g fill="none" stroke="#111" stroke-width="1.3"><circle cx="8" cy="8" r="6.5"/><ellipse cx="8" cy="8" rx="2.8" ry="6.5"/><path d="M1.5 8 H14.5 M2.6 4.5 H13.4 M2.6 11.5 H13.4"/></g></svg>
          <span>www.velorashop.example</span>
        </li>
        <li>
          <svg viewBox="0 0 16 16" aria-hidden="true"><rect x="2" y="2" width="12" height="12" fill="none" stroke="#111" stroke-width="1.4"/></svg>
          <span>velora_</span>
        </li>
      </ul>
      <p class="address">318 W. Prior St #27, #109<br>Los Angeles, CA 90099</p>
    </div>
  </section>

</main>
</body>
</html>
```